FR banner

we need a banner design (36"x120" horizontal) that will be displayed on a local high school baseball field. My company ( Crestwell Prints Co) has been producing signage for the Fernmoor Ridge community since 2009. We would like to communicate that we do more than banners. The final design should include the slogan "Signs Shirts Swag" and our Logo.

Target Market(s)

companies, teams, events, shirt and other marketing items.

Industry/Entity Type

Sign, Print,

Font styles to use
Sans Serif

Requirements
Should not have
• no baseball content.

```html
<!DOCTYPE html>
<html lang="en">
<head>
<meta charset="utf-8">
<title>Crestwell Prints Co – Field Banner</title>
<link rel="stylesheet" href="https://fonts.googleapis.com/css2?family=Outfit:wght@800&display=swap">
<style>
  :root {
    --backdrop: #8c8c8c;
    --banner-white: #ffffff;
    --banner-black: #000000;
  }
  html, body {
    margin: 0;
    padding: 0;
    width: 1200px;
    height: 1200px;
    overflow: hidden;
    background: var(--backdrop);
  }
  .canvas {
    position: relative;
    width: 1200px;
    height: 1200px;
  }
  .banner {
    position: absolute;
    left: 78px;
    top: 447px;
    width: 1044px;
    height: 313px;
    background: var(--banner-white);
    overflow: hidden;
  }
  .banner-waves {
    position: absolute;
    inset: 0;
    width: 1044px;
    height: 313px;
  }
  .banner-waves path { fill: var(--banner-black); }
  .brand {
    position: absolute;
    left: 0;
    right: 0;
    top: 88px;
    display: flex;
    justify-content: center;
    align-items: center;
    gap: 12px;
    font-family: "Outfit", sans-serif;
    font-weight: 800;
    font-size: 32px;
    letter-spacing: 0.5px;
    color: var(--banner-black);
    white-space: nowrap;
  }
  .brand-mark {
    width: 22px;
    height: 22px;
    background: var(--banner-black);
  }
  .slogan {
    position: absolute;
    left: 0;
    right: 0;
    top: 200px;
    margin: 0;
    text-align: center;
    font-family: "Outfit", sans-serif;
    font-weight: 800;
    font-size: 86px;
    line-height: 1;
    letter-spacing: 1px;
    color: var(--banner-white);
    white-space: nowrap;
  }
</style>
</head>
<body>
<div class="canvas">
  <section class="banner">
    <svg class="banner-waves" viewBox="0 0 1044 313" aria-hidden="true">
      <path class="wave-body" d="M0,155 C200,185 450,190 600,180 C800,168 950,160 1044,172 L1044,313 L0,313 Z"/>
      <path class="wave-swoosh-left" d="M0,128 C150,160 280,178 340,181 C250,180 120,170 0,148 Z"/>
      <path class="wave-swoosh-right" d="M640,156 C820,138 960,128 1044,138 L1044,163 C950,150 800,152 640,156 Z"/>
    </svg>
    <div class="brand">
      <span class="brand-mark"></span>
      <span class="brand-name">Crestwell Prints Co</span>
    </div>
    <h1 class="slogan">SIGNS SHIRTS SWAG</h1>
  </section>
</div>
</body>
</html>
```